Marcus Delvecchio Wellness podcast

I have overcome many health challenges. All of them have put me in position to help other people do the same. Eventually I became a certified health coach through the Academy of Integrative Nourishment. I have a strong desire to help because I know what it’s like to not feel well, and do what you want. The content on this sight will equip you with the tools to live a life full of health, freedom, and happiness. Complex health topics are broken down into simple ways to understand. No wellness topic is off limits, whether its heart disease, cancer, diabetes, sleep, hormones, or any other wellness topic.

Target Market(s)

People who are interested in growth and getting healthier

Industry/Entity Type

Health and Wellness

Colors
0054AA
0677BA
7BADD7
CADEEF
E8F1F8
0094D4
00A9DD
6FCCEA
C7EBF8
E9F6FB

Requirements

```html
<!DOCTYPE html>
<html lang="en">
<head>
<meta charset="utf-8">
<title>Marcus Delvecchio Wellness Podcast</title>
<link href="https://fonts.googleapis.com/css2?family=Anton&family=Great+Vibes&family=Poppins:wght@500&display=swap" rel="stylesheet">
<style>
  :root {
    --navy-deep: #05315e;
    --navy: #0b4c85;
    --blue-mid: #1a6aa6;
    --lime: #dfff00;
    --white: #ffffff;
    --outline-blue: #0a5a91;
    --portrait-light: #d6d6d6;
    --portrait-dark: #8e8e8e;
  }
  html, body {
    margin: 0;
    width: 1200px;
    height: 1200px;
    overflow: hidden;
    background: var(--navy);
  }
  .cover {
    display: block;
    width: 1200px;
    height: 1200px;
  }
  .title-name {
    font-family: "Anton", "Oswald", sans-serif;
    fill: var(--lime);
  }
  .title-script {
    font-family: "Great Vibes", cursive;
    fill: var(--white);
    stroke: var(--outline-blue);
    stroke-width: 12px;
    stroke-linejoin: round;
    paint-order: stroke fill;
  }
  .label-podcast {
    font-family: "Poppins", sans-serif;
    font-weight: 500;
    fill: var(--white);
  }
  .frame-line {
    stroke: var(--white);
    stroke-width: 3;
    fill: none;
  }
</style>
</head>
<body>
<svg class="cover" viewBox="0 0 1200 1200" xmlns="http://www.w3.org/2000/svg">
  <defs>
    <radialGradient id="bg-glow" cx="50%" cy="42%" r="75%">
      <stop offset="0%" stop-color="var(--blue-mid)"/>
      <stop offset="60%" stop-color="var(--navy)"/>
      <stop offset="100%" stop-color="var(--navy-deep)"/>
    </radialGradient>
    <linearGradient id="portrait-tone" x1="0" y1="0" x2="0" y2="1">
      <stop offset="0%" stop-color="var(--portrait-dark)"/>
      <stop offset="35%" stop-color="var(--portrait-light)"/>
      <stop offset="100%" stop-color="#c4c4c4"/>
    </linearGradient>
  </defs>

  <rect class="background" width="1200" height="1200" fill="url(#bg-glow)"/>

  <g class="frame">
    <line class="frame-line" x1="122" y1="131" x2="1077" y2="131"/>
    <line class="frame-line" x1="122" y1="130" x2="122" y2="229"/>
    <line class="frame-line" x1="122" y1="837" x2="122" y2="915"/>
    <line class="frame-line" x1="121" y1="914" x2="626" y2="914"/>
    <line class="frame-line" x1="1077" y1="130" x2="1077" y2="324"/>
  </g>

  <path class="host-portrait" role="img" aria-label="Black and white cut-out photo of the podcast host, smiling, wearing a t-shirt"
        d="M852 420 C860 360 900 300 990 290 C1080 290 1130 340 1140 430
           C1135 500 1110 540 1090 560 C1075 590 1060 610 1062 640
           L1070 700 C1120 720 1180 735 1200 745 L1200 1200 L588 1200
           C592 1080 605 960 640 880 C670 810 720 760 790 725
           C820 712 850 705 862 695 L868 640 C858 600 852 520 852 420 Z"
        fill="url(#portrait-tone)" stroke="var(--white)" stroke-width="6"/>

  <text class="title-name" x="79" y="462" font-size="234" textLength="771" lengthAdjust="spacingAndGlyphs">MARCUS</text>
  <text class="title-name" x="79" y="642" font-size="194" textLength="771" lengthAdjust="spacingAndGlyphs">DELVECCHIO</text>
  <text class="title-script" x="90" y="815" font-size="228" textLength="728" lengthAdjust="spacingAndGlyphs">Wellness</text>

  <text class="label-podcast" x="92" y="1058" font-size="40" textLength="262" lengthAdjust="spacing">PODCAST</text>
</svg>
</body>
</html>
```